Corporate Business Card

Very professional, Modern, Not to busy, include phone address email, website
(541) 555-0174, 61807 19th Street N, Harlow Bay, OR 98517, marcus@kestrelbayholding.com, brelvanindustries.com

Target Market(s)

Manufacturing

Industry/Entity Type

Aero, machining, manufacturing, Off road racing

Contact Information for Business Card

Phone, address email, website

```html
<!DOCTYPE html>
<html lang="en">
<head>
<meta charset="utf-8">
<title>Brelvan Industries — Business Card</title>
<link href="https://fonts.googleapis.com/css2?family=Nunito+Sans:wght@400;700;800&display=swap" rel="stylesheet">
<style>
  :root {
    --navy: #16346e;
    --red: #d2232a;
    --ink: #2b2b2b;
    --paper: #ffffff;
    --backdrop: #d9d9d9;
  }
  * { box-sizing: border-box; margin: 0; padding: 0; }
  html, body { width: 1200px; height: 1018px; overflow: hidden; }
  body {
    background: var(--backdrop);
    font-family: "Nunito Sans", sans-serif;
    display: flex;
    flex-direction: column;
    align-items: center;
    justify-content: center;
    gap: 60px;
  }
  .card {
    position: relative;
    width: 700px;
    height: 400px;
    overflow: hidden;
    box-shadow: 0 6px 18px rgba(0,0,0,0.18);
  }
  .card--front { background: var(--paper); }
  .card--back { background: var(--navy); display: flex; align-items: center; justify-content: center; }

  .timeline { position: absolute; left: 0; top: 0; width: 700px; height: 400px; }

  .identity { position: absolute; left: 84px; top: 38px; }
  .identity__name { color: var(--navy); font-weight: 800; font-size: 30px; line-height: 1; }
  .identity__role { color: var(--ink); font-size: 15px; margin-top: 4px; }

  .contact { position: absolute; left: 84px; color: var(--ink); font-size: 16px; line-height: 1.25; }
  .contact--address { top: 124px; }
  .contact--phone { top: 208px; }
  .contact--email { top: 244px; }
  .contact--web { top: 280px; }

  .wordmark {
    position: absolute;
    right: 60px;
    top: 170px;
    color: var(--navy);
    font-weight: 800;
    font-size: 38px;
    line-height: 1;
    text-align: right;
  }
  .wordmark--back { position: static; color: var(--paper); font-size: 52px; }
  .wordmark-group { display: flex; align-items: center; gap: 18px; }
  .wordmark-square { width: 22px; height: 22px; background: var(--red); }

  .bands { position: absolute; left: 0; bottom: 0; width: 700px; height: 18px; }
</style>
</head>
<body>
  <section class="card card--front" aria-label="Business card front">
    <svg class="timeline" viewBox="0 0 700 400" aria-hidden="true">
      <line x1="46" y1="56" x2="46" y2="292" stroke="#d2232a" stroke-width="1.5"/>
      <polygon points="46,38 62,47 62,65 46,74 30,65 30,47" fill="#d2232a"/>
      <circle cx="46" cy="51" r="5" fill="#fff"/>
      <path d="M36 66 Q46 54 56 66 Z" fill="#fff"/>
      <polygon points="46,122 57,128 57,140 46,146 35,140 35,128" fill="#d2232a"/>
      <path d="M46 141 L41 133 A5 5 0 1 1 51 133 Z" fill="#fff"/>
      <circle cx="46" cy="131" r="1.8" fill="#d2232a"/>
      <polygon points="46,205 57,211 57,223 46,229 35,223 35,211" fill="#d2232a"/>
      <path d="M41 212 L44 212 L45 215 L43.5 216.5 Q45 219.5 47.5 220.5 L49 219 L52 220 L52 223 Q42 223 41 212 Z" fill="#fff"/>
      <polygon points="46,241 57,247 57,259 46,265 35,259 35,247" fill="#d2232a"/>
      <rect x="40" y="249" width="12" height="8" fill="#fff"/>
      <path d="M40 249 L46 254 L52 249" fill="none" stroke="#d2232a" stroke-width="1"/>
      <polygon points="46,277 57,283 57,295 46,301 35,295 35,283" fill="#d2232a"/>
      <circle cx="46" cy="289" r="6" fill="none" stroke="#fff" stroke-width="1.5"/>
      <line x1="40" y1="289" x2="52" y2="289" stroke="#fff" stroke-width="1.2"/>
      <ellipse cx="46" cy="289" rx="2.5" ry="6" fill="none" stroke="#fff" stroke-width="1.2"/>
    </svg>

    <div class="identity">
      <h1 class="identity__name">Dalen Corwick</h1>
      <p class="identity__role">Founder</p>
    </div>

    <p class="contact contact--address">61807 19th Street N,<br>Harlow Bay, OR 98517</p>
    <p class="contact contact--phone">(541) 555-0174</p>
    <p class="contact contact--email">marcus@kestrelbayholding.com</p>
    <p class="contact contact--web">www.brelvanindustries.com</p>

    <div class="wordmark">Brelvan<br>Industries</div>

    <svg class="bands" viewBox="0 0 700 18" preserveAspectRatio="none" aria-hidden="true">
      <polygon points="0,0 300,0 286,18 0,18" fill="#16346e"/>
      <polygon points="312,0 700,0 700,18 298,18" fill="#d2232a"/>
    </svg>
  </section>

  <section class="card card--back" aria-label="Business card back">
    <div class="wordmark-group">
      <span class="wordmark-square" aria-hidden="true"></span>
      <span class="wordmark wordmark--back">Brelvan Industries</span>
    </div>
  </section>
</body>
</html>
```